Finally a Vodka produced for women ! (Label Design)

We are a small distillery based in Melbourne, Australia and we need a Vodka label design solution that will appeal to women aged 30-50 years and radiate luxury. Full Details are in a design brief attached. We thank you in advance.

Target Market(s)

Affluent females 30-50 years.

Industry/Entity Type

Spirits/Alcohol

Requirements
Must have
• Be clear this is a luxury Vodka.
Nice to have
• Elegance.

```html
<!DOCTYPE html>
<html lang="en">
<head>
<meta charset="utf-8">
<title>Vodka Premium – Rose Quartz Filtered Label</title>
<link href="https://fonts.googleapis.com/css2?family=Parisienne&family=Playfair+Display:wght@400;700&display=swap" rel="stylesheet">
<style>
  :root {
    --paper: #ffffff;
    --ink: #111111;
    --rose: #e7b3b6;
    --rose-text: #ffffff;
    --muted: #9c9c9c;
  }
  html, body {
    margin: 0;
    padding: 0;
    width: 1200px;
    height: 1000px;
    overflow: hidden;
    background: var(--paper);
  }
  .canvas {
    position: relative;
    width: 1200px;
    height: 1000px;
    background: var(--paper);
    font-family: "Playfair Display", Georgia, serif;
  }
  .label {
    position: absolute;
    left: 100px;
    top: 180px;
    width: 535px;
    text-align: center;
  }
  .wordmark {
    position: relative;
    height: 190px;
  }
  .wordmark__script {
    display: block;
    font-family: "Parisienne", cursive;
    font-size: 158px;
    line-height: 1;
    color: var(--ink);
    margin-top: 10px;
    letter-spacing: -2px;
  }
  .wordmark__tier {
    position: absolute;
    left: 0;
    right: 0;
    top: 158px;
    font-size: 20px;
    font-weight: 700;
    letter-spacing: 2px;
    color: var(--ink);
    margin-left: -10px;
  }
  .banner {
    position: relative;
    width: 500px;
    height: 63px;
    margin: 101px auto 0;
  }
  .banner__shape {
    position: absolute;
    inset: 0;
  }
  .banner__text {
    position: relative;
    line-height: 63px;
    font-size: 26px;
    font-weight: 700;
    letter-spacing: 2.5px;
    color: var(--rose-text);
  }
  .origin {
    margin: 33px 0 0;
    font-size: 18px;
    line-height: 22px;
    letter-spacing: 1.6px;
    color: var(--muted);
  }
  .maker {
    margin: 20px auto 0;
    width: 120px;
    color: var(--ink);
    font-weight: 700;
  }
  .maker__line {
    display: block;
    font-size: 19px;
    line-height: 22px;
    letter-spacing: 5px;
  }
  .maker__sub {
    display: block;
    font-size: 8px;
    line-height: 12px;
    letter-spacing: 4.2px;
  }
  .specs {
    margin: 62px 0 0;
    font-size: 15px;
    line-height: 18px;
    letter-spacing: 1px;
    color: var(--muted);
  }
  .neck-strip {
    position: absolute;
    left: 1001px;
    top: 166px;
    width: 70px;
    height: 264px;
  }
</style>
</head>
<body>
  <main class="canvas">
    <section class="label">
      <div class="wordmark">
        <span class="wordmark__script">Vodka</span>
        <span class="wordmark__tier">PREMIUM</span>
      </div>

      <div class="banner">
        <svg class="banner__shape" viewBox="0 0 500 63" preserveAspectRatio="none" aria-hidden="true">
          <polygon points="25,0 475,0 500,63 0,63" fill="var(--rose)"/>
        </svg>
        <div class="banner__text">ROSE QUARTZ FILTERED</div>
      </div>

      <p class="origin">Handcrafted in<br>Melbourne, Australia</p>

      <div class="maker">
        <span class="maker__line">SILVER</span>
        <span class="maker__line">WREN</span>
        <span class="maker__sub">DISTILLERY</span>
      </div>

      <p class="specs">40% Alc/Vol<br>700ml</p>
    </section>

    <svg class="neck-strip" viewBox="0 0 70 264" role="img" aria-label="Rose neck strip with chevron pattern and round seal">
      <rect x="20" y="0" width="30" height="264" fill="var(--rose)"/>
      <circle cx="35" cy="132" r="33" fill="var(--rose)"/>
    </svg>
  </main>
</body>
</html>
```